Brookvale Systems Yellow rose letterhead

I have a new logo for my company but in its current form it is too large to be used on letterhead or as a email signature. I need to have the designer use elements from the current logo and create something close to the original but more suited for smaller items.
Updates

I just uploaded a copy of our logo that does not have the weathered affect. Thanks

Industry/Entity Type

It Company

Requirements
Must have
• The design must maintain the visual effect of the current logo. It needs to include the yellow rose and the name of the company.
Nice to have
• It would be nice to maintain the stamp theme and incorporate my name, address, phone, email. etc.

```html
<!DOCTYPE html>
<html lang="en">
<head>
<meta charset="utf-8">
<title>Brookvale Systems Letterhead</title>
<link href="https://fonts.googleapis.com/css2?family=Arimo:wght@400;700&display=swap" rel="stylesheet">
<style>
  :root {
    --backdrop: #b9b9b9;
    --paper: #ffffff;
    --bark: #5a4a42;
    --teal: #3bb3b3;
    --sun: #f6c21c;
    --orange: #f2a23a;
    --ink-light: #ffffff;
  }
  * { margin: 0; padding: 0; box-sizing: border-box; }
  html, body {
    width: 848px;
    height: 1200px;
    overflow: hidden;
    background: var(--backdrop);
    font-family: "Arimo", Arial, sans-serif;
  }
  .letterhead {
    position: absolute;
    left: 107px;
    top: 153px;
    width: 633px;
    height: 895px;
    background: var(--paper);
  }
  .header-band {
    position: absolute;
    left: 0; top: 0;
    width: 100%;
    height: 76px;
    background: var(--bark);
  }
  .trim {
    position: absolute;
    left: 0;
    width: 100%;
    height: 7px;
    background: linear-gradient(to bottom,
      var(--orange) 0 2px,
      var(--paper) 2px 3px,
      var(--teal) 3px 5px,
      var(--paper) 5px 7px);
  }
  .trim--top { top: 76px; }
  .trim--bottom { top: 829px; transform: scaleY(-1); }
  .brand-mark {
    position: absolute;
    left: 18px;
    top: 12px;
    width: 100px;
    height: 100px;
    border-radius: 50%;
    background: var(--sun);
  }
  .brand-name {
    position: absolute;
    left: 172px;
    top: 18px;
    font-size: 27px;
    font-weight: 700;
    color: var(--teal);
    letter-spacing: 0.5px;
    white-space: nowrap;
  }
  .brand-tagline {
    position: absolute;
    left: 173px;
    top: 51px;
    font-size: 16px;
    font-weight: 400;
    color: var(--ink-light);
    letter-spacing: 1.2px;
    white-space: nowrap;
  }
  .footer-band {
    position: absolute;
    left: 0;
    top: 835px;
    width: 100%;
    height: 60px;
    background: var(--bark);
    color: var(--ink-light);
    font-size: 12.5px;
  }
  .contact-address {
    position: absolute;
    left: 36px;
    top: 12px;
    white-space: nowrap;
  }
  .contact-line {
    position: absolute;
    left: 36px;
    top: 32px;
    display: flex;
    align-items: center;
    white-space: nowrap;
  }
  .contact-line svg { display: block; }
  .contact-email { margin-left: 16px; }
  .contact-phone-icon { margin-left: 18px; }
  .contact-phone { margin-left: 14px; }
  .signatory {
    position: absolute;
    right: 13px;
    top: 14px;
    font-weight: 700;
    font-size: 13px;
    white-space: nowrap;
  }
</style>
</head>
<body>
  <main class="letterhead">
    <header class="header-band">
      <span class="brand-name">Brookvale Systems</span>
      <span class="brand-tagline">Planning systems that last</span>
    </header>
    <div class="trim trim--top"></div>
    <div class="brand-mark" aria-hidden="true"></div>

    <div class="trim trim--bottom"></div>
    <footer class="footer-band">
      <p class="contact-address">214 Willow Creek Road, Ste 1180, Cedar Ford, TX 76520</p>
      <p class="contact-line">
        <svg width="20" height="14" viewBox="0 0 20 14" aria-label="Email">
          <rect x="0.75" y="0.75" width="18.5" height="12.5" fill="none" stroke="#fff" stroke-width="1.2"/>
          <path d="M1 1 L10 8 L19 1 M1 13 L7.5 6 M19 13 L12.5 6" fill="none" stroke="#fff" stroke-width="1.2"/>
        </svg>
        <span class="contact-email">nora@brookvale-systems.com</span>
        <svg class="contact-phone-icon" width="18" height="14" viewBox="0 0 18 14" aria-label="Phone">
          <path d="M1 5 C1 1 17 1 17 5 L17 6 L13 6 L13 4 L5 4 L5 6 L1 6 Z" fill="#fff"/>
          <path d="M4 7 L14 7 L16 13 L2 13 Z" fill="#fff"/>
          <circle cx="9" cy="10" r="1.8" fill="#5a4a42"/>
        </svg>
        <span class="contact-phone">1-800-555-0142</span>
      </p>
      <p class="signatory">Nora Castell, PhD</p>
    </footer>
  </main>
</body>
</html>
```